Geschäftspapiere für Rechnungen, Anschreiben etc.
Zielgruppe
Yogaunterricht - Einzelstunden, Workshops, Seminare etc.
Aufgabenstellung
Es soll weiche Übergänge haben mit dem bestehenden Logo und gerne den Farbverlauf nutzen. Auf das Briefpapier muss der Name, die Adresse, Web- und Emailadresse: www.velin-yoga.com

```html
<!DOCTYPE html>
<html lang="de">
<head>
<meta charset="utf-8">
<title>Velin Yoga – Briefpapier</title>
<link href="https://fonts.googleapis.com/css2?family=Cinzel:wght@400&display=swap" rel="stylesheet">
<style>
  :root {
    --paper: #ffffff;
    --frame: #cfcfcf;
    --ink-grey: #9a9a9a;
    --dot-grey: #cccccc;
    --green-light: #86bf41;
    --green-mid: #6a9a3a;
    --green-dark: #446630;
    --text-light: #e6ecde;
    --ornament-green: #eef4e8;
    --ornament-grey: #ececec;
  }
  html, body {
    margin: 0;
    padding: 0;
    background: var(--paper);
    overflow: hidden;
  }
  .letterhead {
    position: relative;
    width: 863px;
    height: 1200px;
    background: var(--paper);
    box-sizing: border-box;
    border: 1px solid var(--frame);
    overflow: hidden;
  }
  .brand-top {
    position: absolute;
    top: 17px;
    left: 590px;
    width: 250px;
    text-align: center;
  }
  .brand-top__circle {
    display: block;
    width: 108px;
    height: 108px;
    margin: 0 auto;
    border-radius: 50%;
    border: 2px solid #d4d4d4;
    background: #f3f7ef;
    box-sizing: border-box;
  }
  .brand-top__name {
    margin: 14px 0 0;
    font-family: "Cinzel", serif;
    font-weight: 400;
    font-size: 34px;
    letter-spacing: 1px;
    color: var(--ink-grey);
    line-height: 1;
    white-space: nowrap;
  }
  .punch-mark {
    position: absolute;
    left: 13px;
    width: 5px;
    height: 5px;
    border-radius: 50%;
    background: var(--dot-grey);
  }
  .punch-mark--top { top: 343px; }
  .punch-mark--middle { top: 537px; width: 6px; height: 6px; left: 12px; }
  .punch-mark--bottom { top: 731px; }
  .watermark-ornament {
    position: absolute;
    left: 520px;
    top: 355px;
    width: 343px;
    height: 665px;
  }
  .footer-band {
    position: absolute;
    left: 0;
    top: 1040px;
    width: 863px;
    height: 160px;
  }
  .footer-band__name {
    position: absolute;
    left: 390px;
    top: 1085px;
    width: 440px;
    margin: 0;
    text-align: right;
    font-family: "Cinzel", serif;
    font-weight: 400;
    font-size: 60px;
    letter-spacing: 2px;
    color: var(--text-light);
    line-height: 1;
    white-space: nowrap;
  }
</style>
</head>
<body>
  <main class="letterhead">
    <header class="brand-top">
      <span class="brand-top__circle"></span>
      <p class="brand-top__name">VELIN YOGA</p>
    </header>

    <span class="punch-mark punch-mark--top"></span>
    <span class="punch-mark punch-mark--middle"></span>
    <span class="punch-mark punch-mark--bottom"></span>

    <svg class="watermark-ornament" viewBox="0 0 343 665" role="img" aria-label="Große, sehr blasse Mandala-Verzierung am rechten Rand">
      <defs>
        <radialGradient id="ornamentFade" cx="343" cy="333" r="330" gradientUnits="userSpaceOnUse">
          <stop offset="0" stop-color="var(--ornament-grey)"/>
          <stop offset="0.45" stop-color="var(--ornament-green)"/>
          <stop offset="1" stop-color="#ffffff" stop-opacity="0"/>
        </radialGradient>
      </defs>
      <rect width="343" height="665" fill="url(#ornamentFade)"/>
    </svg>

    <svg class="footer-band" viewBox="0 1040 863 160" preserveAspectRatio="none">
      <defs>
        <linearGradient id="bandGradient" x1="0" y1="0" x2="1" y2="0">
          <stop offset="0" stop-color="var(--green-light)"/>
          <stop offset="0.5" stop-color="var(--green-mid)"/>
          <stop offset="1" stop-color="var(--green-dark)"/>
        </linearGradient>
        <radialGradient id="cornerFade" cx="0" cy="1130" r="100" gradientUnits="userSpaceOnUse">
          <stop offset="0" stop-color="#d9e9c6"/>
          <stop offset="0.7" stop-color="#b7d68f" stop-opacity="0.6"/>
          <stop offset="1" stop-color="#9ccb62" stop-opacity="0"/>
        </radialGradient>
      </defs>
      <path d="M260,1057 Q560,1048 863,1051 L863,1057 Q560,1053 260,1057 Z" fill="var(--green-dark)"/>
      <path d="M0,1055 Q430,1058 863,1062 L863,1200 L0,1200 Z" fill="url(#bandGradient)"/>
      <rect x="0" y="1060" width="100" height="140" fill="url(#cornerFade)" role="img" aria-label="Helle Mandala-Verzierung in der linken unteren Ecke"/>
    </svg>
    <p class="footer-band__name">VELIN YOGA</p>
  </main>
</body>
</html>
```